brightmesh Business Card

Already have the logo, but now need the business card design

Industry/Entity Type

Business Software

Contact Information for Business Card

web site will be brightmesh.io / The card should have the person name / position / mobile / email / and company address

Colors

Designer to choose colors to be used in the design.

Requirements
Must have
• See business card details
• One side to have the brightmesh logo
Nice to have
• If possible the 'O' from flow can be watermarked into the second side
• Try to fit in the words brightmesh Business Solutions

```html
<!DOCTYPE html>
<html lang="en">
<head>
<meta charset="utf-8">
<title>brightmesh Business Card</title>
<link rel="stylesheet" href="https://fonts.googleapis.com/css2?family=Roboto:wght@400;500&family=Quicksand:wght@500&family=Montserrat:wght@700&display=swap">
<style>
  :root {
    --backdrop: #e4e4e4;
    --card-grey: #595959;
    --card-white: #f4f4f4;
    --accent-red: #e3141b;
    --text-light: #ffffff;
    --text-soft: #e6e6e6;
    --text-dark: #4a4a4a;
  }
  html, body {
    margin: 0;
    width: 1200px;
    height: 852px;
    overflow: hidden;
    background: var(--backdrop);
  }
  .sheet {
    position: relative;
    width: 1200px;
    height: 852px;
  }
  .card {
    position: absolute;
    top: 283px;
    width: 500px;
    height: 286px;
    border-radius: 22px;
    overflow: hidden;
    background: var(--card-grey);
    box-shadow: 0 3px 10px rgba(0,0,0,0.18);
  }
  .card-front { left: 70px; }
  .card-back { left: 630px; }

  .front-brand {
    position: absolute;
    left: 0; right: 0; top: 92px;
    text-align: center;
  }
  .brand-name {
    font-family: 'Quicksand', sans-serif;
    font-weight: 500;
    font-size: 66px;
    line-height: 1;
    color: var(--text-light);
    letter-spacing: -1px;
  }
  .brand-tagline {
    margin-top: 6px;
    font-family: 'Montserrat', sans-serif;
    font-weight: 700;
    font-size: 15px;
    letter-spacing: 2px;
    color: var(--accent-red);
  }

  .back-shapes {
    position: absolute;
    inset: 0;
  }
  .back-brand {
    position: absolute;
    left: 330px;
    top: 60px;
    width: 170px;
    text-align: center;
    transform: rotate(180deg);
  }
  .back-brand .brand-name {
    font-size: 36px;
    color: var(--text-dark);
  }
  .back-brand .brand-tagline {
    font-size: 8px;
    letter-spacing: 1.4px;
    color: var(--text-dark);
    margin-top: 3px;
  }

  .holder {
    position: absolute;
    left: 40px;
    top: 58px;
    font-family: 'Roboto', sans-serif;
    color: var(--text-light);
  }
  .holder-name { font-size: 21px; font-weight: 500; }
  .holder-role { font-size: 12px; color: var(--text-soft); margin-top: 3px; margin-left: 12px; }

  .address {
    position: absolute;
    left: 40px;
    top: 160px;
    font-family: 'Roboto', sans-serif;
    font-size: 12.5px;
    line-height: 17px;
    color: var(--text-soft);
  }
  .contacts {
    position: absolute;
    left: 54px;
    top: 200px;
    margin: 0;
    padding: 0;
    list-style: none;
    font-family: 'Roboto', sans-serif;
    font-size: 12.5px;
    color: var(--text-soft);
  }
  .contacts li {
    display: flex;
    align-items: center;
    gap: 10px;
    height: 18px;
  }
  .contacts svg { width: 11px; height: 11px; fill: var(--text-soft); }
</style>
</head>
<body>
<main class="sheet">

  <section class="card card-front" aria-label="Card front">
    <div class="front-brand">
      <div class="brand-name">brightmesh</div>
      <div class="brand-tagline">BUSINESS SOLUTIONS</div>
    </div>
  </section>

  <section class="card card-back" aria-label="Card back">
    <svg class="back-shapes" viewBox="0 0 500 286" width="500" height="286">
      <path d="M305,0 C285,120 320,225 440,286 L500,286 L500,0 Z" fill="var(--accent-red)"/>
      <path d="M315,0 C296,118 332,222 452,286 L500,286 L500,0 Z" fill="var(--card-white)"/>
      <path d="M0,40 C14,48 20,66 20,90 L0,90 Z" fill="var(--accent-red)"/>
    </svg>

    <div class="back-brand">
      <div class="brand-name">brightmesh</div>
      <div class="brand-tagline">BUSINESS SOLUTIONS</div>
    </div>

    <div class="holder">
      <div class="holder-name">Daniel Reyes</div>
      <div class="holder-role">Administrator</div>
    </div>

    <div class="address">
      1234, Any Street, Any Town,<br>Any City, Country 0000
    </div>

    <ul class="contacts">
      <li>
        <svg viewBox="0 0 12 12"><path d="M1,4 Q6,0 11,4 L9,6 L8,4 Q6,3 4,4 L3,6 Z M2,7 H10 V11 H2 Z"/></svg>
        <span>555-214-0386</span>
      </li>
      <li>
        <svg viewBox="0 0 12 12"><path d="M1,2 H11 V10 H1 Z M1.5,2.5 L6,6.5 L10.5,2.5" stroke="var(--card-grey)" stroke-width="1"/></svg>
        <span>admin@brightmesh.io</span>
      </li>
      <li>
        <svg viewBox="0 0 12 12"><circle cx="6" cy="6" r="5.5"/><path d="M0.5,6 H11.5 M6,0.5 V11.5 M6,0.5 Q2,6 6,11.5 M6,0.5 Q10,6 6,11.5" stroke="var(--card-grey)" stroke-width="0.8" fill="none"/></svg>
        <span>www.brightmesh.io</span>
      </li>
    </ul>
  </section>

</main>
</body>
</html>
```